Custom Cabinet Shop Needs a website design

Hi,
We need a website for a Custom Cabinet Shop and Cabinet parts manufacturing business.
The business has two sides to it. One side provides custom Kitchens, vanities, entertainment units, offices and what not to homeowners and contractors.
The 2nd side of the business provides built to order cabinet boxes and other parts required to put together a project to other cabinet shops, small contractors looking to install there own cabinets.
Website will need a Gallery to display work.
Color scheme to go well with logo.
current website is www.brindlemoorcustomcabinets.com
being changed to www.brindlemoor.ca
Tagline "Joinery with Spirit"
Mission Statement "Our passion is to deliver inspired cabinetry solutions to suit all your needs, supported by our phenomenal star class customer service"
The website should convey quality and professionalism.
Thank you.
Target Market(s)
Homeowners/ Contractors
Industry/Entity Type
Entertainment
Coding
Coded - Design and coding required
Number of Pages Required
1 page
Look and feel
Each slider illustrates characteristics of the customer's brand and the style your logo design should communicate.

```html
<!DOCTYPE html>
<html lang="en">
<head>
<meta charset="utf-8">
<title>Brindlemoor Custom Cabinets</title>
<link href="https://fonts.googleapis.com/css2?family=Noto+Serif:ital,wght@0,400;0,700;1,400;1,700&display=swap" rel="stylesheet">
<style>
  :root {
    --ink: #141414;
    --white: #ffffff;
    --accent: #e2782e;
    --panel: rgba(236, 226, 216, 0.72);
    --panel-dark: rgba(214, 198, 184, 0.7);
    --sand: #c9b6a6;
    --sand-deep: #a8927f;
    --footer-ink: #5b4f46;
    --input-line: #8d7a6c;
  }
  * { box-sizing: border-box; margin: 0; padding: 0; }
  html, body { width: 1200px; height: 2995px; overflow: hidden; }
  body { font-family: "Noto Serif", Georgia, serif; color: var(--ink); position: relative; background: var(--sand); }
  .photo { position: absolute; }
  section { position: absolute; left: 0; width: 1200px; overflow: hidden; }

  /* Hero */
  .hero { top: 0; height: 672px; }
  .hero .photo { inset: 0; background:
      radial-gradient(ellipse at 65% 35%, rgba(190,120,70,.55), transparent 55%),
      radial-gradient(ellipse at 20% 60%, rgba(30,50,80,.8), transparent 60%),
      linear-gradient(180deg, #2b2624 0%, #5a3a26 55%, #3a2416 100%); }
  .nav-bar { position: absolute; top: 0; left: 0; width: 1200px; height: 62px; background: rgba(20,20,20,.35); }
  .brand { position: absolute; left: 160px; top: 14px; display: flex; align-items: center; gap: 8px; color: var(--white); font-weight: 700; font-size: 19px; letter-spacing: 1px; }
  .brand-dot { width: 14px; height: 14px; background: var(--accent); border-radius: 50%; }
  .nav { position: absolute; top: 24px; left: 696px; display: flex; gap: 28px; list-style: none; }
  .nav li { font-size: 11px; font-weight: 700; color: var(--white); text-transform: uppercase; letter-spacing: .3px; }
  .nav li.current { color: var(--accent); }
  .hero-title { position: absolute; top: 290px; width: 100%; text-align: center; color: var(--white); font-size: 52px; font-weight: 400; letter-spacing: 4px; text-shadow: 0 2px 6px rgba(0,0,0,.5); }
  .hero-title em { font-weight: 700; }
  .mission { position: absolute; top: 386px; left: 240px; width: 740px; text-align: center; color: var(--white); font-size: 20px; line-height: 32px; letter-spacing: .6px; text-shadow: 0 1px 4px rgba(0,0,0,.6); }
  .btn-ghost { position: absolute; top: 512px; left: 514px; width: 184px; height: 40px; border-radius: 20px; background: rgba(180,170,160,.45); color: var(--white); font-size: 16px; display: flex; align-items: center; justify-content: center; }

  /* Content panels */
  .about { top: 672px; height: 648px; }
  .about .photo { inset: 0; background: linear-gradient(90deg, #d9d3c8 0%, #e8e4dc 30%, #cfc8bc 60%, #b7b2aa 100%); }
  .services { top: 1320px; height: 624px; }
  .services .photo { inset: 0; background: linear-gradient(180deg, #6f5a4b 0%, #85705f 35%, #c9bfb4 60%, #d3cbc3 80%, #6b5648 100%); }
  .panel { position: absolute; background: var(--panel); border-radius: 16px; text-align: center; }
  .about .panel { left: 528px; top: 104px; width: 512px; height: 434px; }
  .services .panel { left: 166px; top: 108px; width: 510px; height: 412px; background: var(--panel-dark); }
  .panel h2 { font-size: 42px; font-weight: 400; margin-top: 42px; }
  .panel p { font-size: 16px; line-height: 28px; margin: 0 auto; }
  .about .panel p { width: 400px; margin-top: 36px; }
  .about .panel p + p { margin-top: 24px; }
  .services .panel h3 { font-size: 16px; font-weight: 700; margin-top: 22px; letter-spacing: .5px; }
  .services .panel h3:first-of-type { margin-top: 22px; }
  .btn-solid { display: inline-flex; align-items: center; justify-content: center; width: 164px; height: 40px; background: var(--white); border-radius: 20px; font-size: 14px; }
  .about .btn-solid { margin-top: 48px; }
  .services .btn-solid { margin-top: 38px; }

  /* Gallery */
  .gallery { top: 1944px; height: 624px; background: var(--white); }
  .gallery .g1 { left: 0; top: 32px; width: 336px; height: 592px; background: linear-gradient(180deg, #3d352f 0%, #1c1a19 45%, #6c6862 100%); }
  .gallery .g2 { left: 344px; top: 32px; width: 514px; height: 592px; background: linear-gradient(180deg, #e8e3da 0%, #b5a999 45%, #4a3226 80%, #2a1d16 100%); }
  .gallery .g3 { left: 866px; top: 32px; width: 334px; height: 592px; background: linear-gradient(180deg, #e6e2dc 0%, #d9d1c6 45%, #5c3e2d 80%, #c8c0b6 100%); }
  .arrow { position: absolute; top: 290px; width: 60px; height: 52px; background: rgba(210,200,190,.8); border-radius: 10px; display: flex; align-items: center; justify-content: center; }
  .arrow.prev { left: 260px; }
  .arrow.next { left: 884px; }
  .gallery-label { position: absolute; left: 458px; top: 240px; width: 304px; height: 150px; background: rgba(236,226,216,.7); border-radius: 16px; display: flex; align-items: center; justify-content: center; font-size: 42px; font-weight: 400; }

  /* Contact */
  .contact { top: 2568px; height: 427px; background: var(--sand); }
  .contact-watermark { position: absolute; left: 170px; top: 120px; width: 960px; text-align: center; font-size: 110px; font-weight: 700; color: var(--sand-deep); opacity: .25; letter-spacing: 6px; }
  .contact h2 { position: absolute; top: 66px; width: 100%; text-align: center; font-size: 42px; font-weight: 400; }
  .contact .lead { position: absolute; top: 136px; width: 100%; text-align: center; font-size: 14px; font-weight: 700; }
  .signup { position: absolute; top: 174px; left: 350px; display: flex; gap: 12px; }
  .signup .field { width: 386px; height: 38px; border: 1px solid var(--input-line); background: rgba(255,255,255,.12); font-size: 12px; color: var(--footer-ink); padding: 11px 20px; }
  .signup .send { width: 114px; height: 38px; border: 1px solid var(--input-line); background: rgba(255,255,255,.12); font-size: 12px; color: var(--footer-ink); display: flex; align-items: center; justify-content: center; }
  .address { position: absolute; left: 162px; top: 296px; font-size: 10px; line-height: 13px; color: var(--footer-ink); }
  .footer-brand { position: absolute; left: 484px; top: 274px; width: 232px; display: flex; align-items: center; justify-content: center; gap: 10px; font-size: 22px; font-weight: 700; color: var(--ink); }
  .footer-brand .brand-dot { width: 18px; height: 18px; }
  .social { position: absolute; left: 926px; top: 296px; display: flex; gap: 12px; list-style: none; }
  .social li { width: 14px; height: 14px; border-radius: 50%; background: #3a322c; }
  .copyright { position: absolute; left: 790px; top: 326px; width: 250px; text-align: right; font-size: 10px; color: var(--footer-ink); }
</style>
</head>
<body>

<section class="hero">
  <div class="photo" role="img" aria-label="Warmly lit custom kitchen with island, bar stools and pendant lights"></div>
  <div class="nav-bar"></div>
  <div class="brand"><span class="brand-dot"></span>BRINDLEMOOR</div>
  <ul class="nav">
    <li class="current">Home</li>
    <li>Gallery</li>
    <li>About us</li>
    <li>Services</li>
    <li>Contact</li>
  </ul>
  <h1 class="hero-title">JOINERY WITH <em>SPIRIT</em></h1>
  <p class="mission">Our passion is to deliver inspired cabinetry solutions to suit all your needs, supported by our phenomenal star class customer service.</p>
  <a class="btn-ghost">Contact us</a>
</section>

<section class="about">
  <div class="photo" role="img" aria-label="Bright kitchen with white shaker cabinets and dark island base"></div>
  <div class="panel">
    <h2>ABOUT US</h2>
    <p>Lorem ipsum dolor sit amet, consectetuer adipiscing elit. Aenean commodo ligula eget dolor.</p>
    <p>Cum sociis natoque penatibus et magnis dis parturient montes, nascetur ridiculus mus.</p>
    <a class="btn-solid">Read more</a>
  </div>
</section>

<section class="services">
  <div class="photo" role="img" aria-label="Modern wood grain wall cabinets with slim metal handles"></div>
  <div class="panel">
    <h2>SERVICES</h2>
    <h3>RESIDENTIAL</h3>
    <p>Sit amet, consectetuer adipiscing elit.</p>
    <h3>BUSINESS</h3>
    <p>Donec quam felis, ultricies nec, pellentesque eu,<br>pretium quis. sem.</p>
    <a class="btn-solid">Read more</a>
  </div>
</section>

<section class="gallery">
  <div class="photo g1" role="img" aria-label="Dark entertainment unit with stone bar front"></div>
  <div class="photo g2" role="img" aria-label="Kitchen with granite island and stainless range hood"></div>
  <div class="photo g3" role="img" aria-label="White kitchen cabinets with wood island"></div>
  <div class="arrow prev"><svg width="14" height="18" viewBox="0 0 14 18"><path d="M10 2 L3 9 L10 16" fill="none" stroke="#222" stroke-width="3"/></svg></div>
  <div class="arrow next"><svg width="14" height="18" viewBox="0 0 14 18"><path d="M4 2 L11 9 L4 16" fill="none" stroke="#222" stroke-width="3"/></svg></div>
  <div class="gallery-label">GALLERY</div>
</section>

<section class="contact">
  <div class="contact-watermark" aria-hidden="true">BRINDLEMOOR</div>
  <h2>CONTACT US</h2>
  <p class="lead">Sign up now for more information about Brindlemoor Custom Cabinets</p>
  <div class="signup">
    <div class="field">Enter your e-mail</div>
    <div class="send">Contact</div>
  </div>
  <p class="address">4120 Alder Ridge Road, Pine Hollow, AB T0X 1A0<br>hello@brindlemoorcabinets.com<br>Tell: 555-010-2840 or 555-010-7316</p>
  <div class="footer-brand"><span class="brand-dot"></span>BRINDLEMOOR</div>
  <ul class="social"><li></li><li></li><li></li><li></li><li></li></ul>
  <p class="copyright">© 2015 Brindlemoor Custom Cabinets. All rights reserved.</p>
</section>

</body>
</html>
```